Print Design Project- raffle tickets

We need 10 print designs for raffle tickets.
Please create one or two as per specs and do more only if I get in touch with you.
The tickets will be given out to elementary school kids for eating fruits and veggies at lunch time.
The tickets need to bright, colorful and cool.
They will contain the logo (provided), a clip art image (not photo) of a cool teen as per description attached and text. I will need two versions of the final copy- one with the stub and one without the stub for each ticket.
The ticket size is 5.13" by 1.88"
The safe size is 4.92" by 1.67"
The tear off stub is 1" from the right.
The stubs will be a solid color- red, orange, yellow, green and indigo (bluish-purple)
Updates

Target Market(s)

5-12 year olds

Industry/Entity Type

School

Requirements
Must have
• The given text, logo provided and text provided.
The designer will need to put in appropriate clip art pictures of teenagers doing related activities like snowboarding, gardening, basketball etc.
The pictures should look 'cool'. We are trying to make healthy eating be 'cool' and these tickets should be 'wanted' by all the kids in the cafeteria. This should drive them to eat fruits and veggies. High on fun factor.

```html
<!DOCTYPE html>
<html lang="en">
<head>
<meta charset="utf-8">
<title>Color Crunch Club – Raffle Tickets</title>
<link rel="stylesheet" href="https://fonts.googleapis.com/css2?family=Luckiest+Guy&family=Archivo+Black&family=Roboto:wght@400&family=Cormorant+SC:wght@500&display=swap">
<style>
  :root {
    --paper: #ffffff;
    --ink: #1a1a1a;
    --stub-yellow: #f7ec26;
    --band-red: #ed1c4f;
    --code-green: #76bd43;
    --code-text: #eef7e4;
  }
  * { box-sizing: border-box; margin: 0; padding: 0; }
  html, body { width: 1200px; height: 736px; overflow: hidden; background: var(--paper); }
  .sheet { position: relative; width: 1200px; height: 736px; }

  .ticket { position: absolute; width: 382px; height: 168px; display: flex; }
  .col-1 { left: 0; } .col-2 { left: 408px; } .col-3 { left: 816px; }
  .row-1 { top: 0; } .row-2 { top: 194px; } .row-3 { top: 373px; } .row-4 { top: 568px; }

  .ticket-body { position: relative; width: 301px; height: 100%; background: var(--paper); }
  .brand {
    position: absolute; left: 12px; top: 8px;
    font-family: "Luckiest Guy", cursive; font-size: 17px; line-height: 17px;
    color: var(--ink); letter-spacing: 0.5px;
  }
  .mascot {
    position: absolute; left: 205px; top: 4px; width: 62px; height: 62px;
    border-radius: 10px;
  }
  .m-orange { background: linear-gradient(135deg, #f6a623, #d94a2b); }
  .m-green  { background: linear-gradient(135deg, #b9e0a4, #6fb24a); }
  .m-blue   { background: linear-gradient(135deg, #9ccaf0, #2d6fb6); }
  .m-red    { background: linear-gradient(135deg, #f3b3a0, #c9352c); }
  .m-gray   { background: linear-gradient(135deg, #e3e8ee, #a6b3c2); }
  .m-yellow { background: linear-gradient(135deg, #fde58a, #e2a92c); }

  .blurb {
    position: absolute; left: 14px; top: 70px; width: 280px;
    font-family: "Luckiest Guy", cursive; font-size: 9.5px; line-height: 14px;
    letter-spacing: 0.4px; color: var(--ink); text-transform: uppercase;
  }
  .site {
    position: absolute; right: 2px; top: 126px;
    font-family: "Roboto", sans-serif; font-size: 12.5px; color: var(--ink);
  }
  .band { position: absolute; left: 0; bottom: 0; width: 100%; height: 22px; background: var(--band-red); }
  .code {
    position: absolute; right: 0; bottom: 0; width: 120px; height: 22px;
    background: var(--code-green); color: var(--code-text);
    font-family: "Cormorant SC", serif; font-size: 11.5px;
    display: flex; align-items: center; justify-content: center;
  }
  .stub {
    width: 81px; height: 100%; background: var(--stub-yellow);
    display: flex; align-items: center; justify-content: center;
  }
  .points {
    transform: rotate(-90deg); white-space: nowrap;
    font-family: "Archivo Black", sans-serif; font-size: 16px; color: var(--ink);
  }
</style>
</head>
<body>
<main class="sheet">

  <article class="ticket col-1 row-1">
    <div class="ticket-body">
      <div class="brand">Color Crunch<br>Club</div>
      <div class="mascot m-orange" role="img" aria-label="Clip art of a teen snowboarding"></div>
      <p class="blurb">Meet Justin. Loves snowboarding, his dog Mocha and strawberries his strawberry smoothie recipe is yummy and gives him the energy to snowboard! Get his favorite smoothie recipe at</p>
      <span class="site">www.CCCkids.com</span>
      <div class="band"></div><div class="code">Access Code: CCC 112</div>
    </div>
    <div class="stub"><span class="points">2 Points</span></div>
  </article>

  <article class="ticket col-2 row-1">
    <div class="ticket-body">
      <div class="brand">Color Crunch<br>Club</div>
      <div class="mascot m-green" role="img" aria-label="Clip art of a cheerful pencil character"></div>
      <p class="blurb">Future author Emma. Loves writing mysteries, swimming and bell peppers dipped in hummus. This tasty snack keeps her fueled and away from writers block! Get her delish hummus recipe at</p>
      <span class="site">www.CCCkids.com</span>
      <div class="band"></div><div class="code">Access Code: CCC 131</div>
    </div>
    <div class="stub"><span class="points">2 Points</span></div>
  </article>

  <article class="ticket col-3 row-1">
    <div class="ticket-body">
      <div class="brand">Color Crunch<br>Club</div>
      <div class="mascot m-blue" role="img" aria-label="Clip art of a girl reading a book"></div>
      <p class="blurb">Laura loves math, her cat Mittens and growing food in her garden. Her favorite herb is basil and she knows how to make a tasty pesto! Get her super recipe at</p>
      <span class="site">www.CCCkids.com</span>
      <div class="band"></div><div class="code">Access Code: CCC 156</div>
    </div>
    <div class="stub"><span class="points">2 Points</span></div>
  </article>

  <article class="ticket col-1 row-2">
    <div class="ticket-body">
      <div class="brand">Color Crunch<br>Club</div>
      <div class="mascot m-gray" role="img" aria-label="Clip art of a young chef baking"></div>
      <p class="blurb">Preston is a chef-in-making! He loves trying new foods from different countries. His favorite dip is guacamole. Look for his lip-smacking guacamole recipe at</p>
      <span class="site">www.CCCkids.com</span>
      <div class="band"></div><div class="code">Access Code: CCC 148</div>
    </div>
    <div class="stub"><span class="points">2 Points</span></div>
  </article>

  <article class="ticket col-2 row-2">
    <div class="ticket-body">
      <div class="brand">Color Crunch<br>Club</div>
      <div class="mascot m-red" role="img" aria-label="Clip art of a lacrosse player"></div>
      <p class="blurb">Raoul's favorite sport is lacrosse and he's working hard to be a research scientist. He eats smart to stay strong; he loves to munch on kale chips that his mom makes. Get the recipe at</p>
      <span class="site">www.CCCkids.com</span>
      <div class="band"></div><div class="code">Access Code: CCC 189</div>
    </div>
    <div class="stub"><span class="points">2 Points</span></div>
  </article>

  <article class="ticket col-3 row-2">
    <div class="ticket-body">
      <div class="brand">Color Crunch<br>Club</div>
      <div class="mascot m-gray" role="img" aria-label="Clip art of a news reporter with a microphone"></div>
      <p class="blurb">Sim is going to be a financial news reporter and loves basketball. She thinks roasted sweet potatoes taste better than dessert. Get her favorite recipe at</p>
      <span class="site">www.CCCkids.com</span>
      <div class="band"></div><div class="code">Access Code: CCC 176</div>
    </div>
    <div class="stub"><span class="points">2 Points</span></div>
  </article>

  <article class="ticket col-1 row-3">
    <div class="ticket-body">
      <div class="brand">Color Crunch<br>Club</div>
      <div class="mascot m-blue" role="img" aria-label="Clip art of a baseball batter"></div>
      <p class="blurb">Science genius Sid loves playing baseball. He never liked veggies until one day when he realized they were superfoods. He now loves to eat a big salad! Learn how he makes his supersalad at</p>
      <span class="site">www.CCCkids.com</span>
      <div class="band"></div><div class="code">Access Code: CCC 107</div>
    </div>
    <div class="stub"><span class="points">2 Points</span></div>
  </article>

  <article class="ticket col-2 row-3">
    <div class="ticket-body">
      <div class="brand">Color Crunch<br>Club</div>
      <div class="mascot m-yellow" role="img" aria-label="Clip art of a young builder with tools"></div>
      <p class="blurb">Ben is rockstar at building stuff! He's going to be an architect and loves to go biking. His favorite snack is a frozen banana shake. Learn how to make this scrumptious shake at</p>
      <span class="site">www.CCCkids.com</span>
      <div class="band"></div><div class="code">Access Code: CCC 140</div>
    </div>
    <div class="stub"><span class="points">2 Points</span></div>
  </article>

  <article class="ticket col-3 row-3">
    <div class="ticket-body">
      <div class="brand">Color Crunch<br>Club</div>
      <div class="mascot m-green" role="img" aria-label="Clip art of a soccer player kicking a ball"></div>
      <p class="blurb">Nick's first love is soccer and he spends a lot of time in the hot sun. He's also pro at making his own electrolyte water. Get his refreshing and smart recipe at</p>
      <span class="site">www.CCCkids.com</span>
      <div class="band"></div><div class="code">Access Code: CCC 166</div>
    </div>
    <div class="stub"><span class="points">2 Points</span></div>
  </article>

  <article class="ticket col-1 row-4">
    <div class="ticket-body">
      <div class="brand">Color Crunch<br>Club</div>
      <div class="mascot m-yellow" role="img" aria-label="Clip art of a girl dancing"></div>
      <p class="blurb">Alina thinks theater and drama are dabomb! She loves dancing and fruity desserts like berry sauce swirled on creamy yogurt. Learn the recipe for her beautiful berry sauce at</p>
      <span class="site">www.CCCkids.com</span>
      <div class="band"></div><div class="code">Access Code: CCC 186</div>
    </div>
    <div class="stub"><span class="points">2 Points</span></div>
  </article>

</main>
</body>
</html>
```